Redesign and move to Wordpress for qorvanta.com

Our website needs a redesign and at the same time we are moving it to Wordpress. Please help us with a new digital professional look and feel.

We are an Australian Software Engineering company specialising in advanced software development using in A.I., PLatform Engineering, Integration and Cloud. See the current qorvanta.com for more information about us.

```html
<!DOCTYPE html>
<html lang="en">
<head>
<meta charset="utf-8">
<title>Qorvanta — Reliable Smart Software Engineering</title>
<link rel="stylesheet" href="https://fonts.googleapis.com/css2?family=Poppins:wght@300;400;500;600;700&family=Oswald:wght@500;600&display=swap">
<style>
:root{
  --navy:#1a4f8b;
  --navy-dark:#163f70;
  --teal:#4fc3bd;
  --teal-light:#7fd6d1;
  --ink:#222;
  --muted:#555;
  --light:#f2f2f2;
  --white:#fff;
}
*{box-sizing:border-box;margin:0;padding:0}
html,body{width:1200px;height:5367px;overflow:hidden;background:var(--white)}
body{font-family:"Poppins",sans-serif;color:var(--ink);position:relative}
.abs{position:absolute}
.btn{position:absolute;display:flex;align-items:center;gap:10px;background:var(--navy);color:var(--white);font-size:14px;font-weight:500;padding:0 8px 0 14px;height:32px;text-transform:uppercase;letter-spacing:.3px}
.btn .sq{width:22px;height:22px;border:2px solid var(--white);display:grid;grid-template-columns:1fr 1fr;gap:2px;padding:2px}
.btn .sq i{border:1.5px solid var(--white)}
.btn.sm{height:28px;font-size:12px}
/* header */
.site-header{position:absolute;top:0;left:0;width:1200px;height:96px;background:var(--white);z-index:2}
.brand{position:absolute;left:70px;top:20px;display:flex;align-items:center;gap:14px}
.brand .mark{width:70px;height:70px;border:3px solid var(--navy)}
.brand span{font-size:30px;font-weight:400;color:var(--navy);letter-spacing:1px}
.nav{position:absolute;top:50px;left:690px;display:flex;gap:48px;font-size:14px;color:var(--navy)}
.nav .active{border-bottom:2px solid var(--navy);padding-bottom:4px}
.nav-contact{position:absolute;left:1032px;top:44px;width:102px;height:30px;background:var(--navy);color:#fff;font-size:14px;display:flex;align-items:center;justify-content:center}
/* hero */
.hero-media{position:absolute;top:96px;left:0;width:1200px;height:704px;background:linear-gradient(100deg,#c9dfe8 0%,#a9cfe0 30%,#3fa9d8 60%,#1f86c8 100%)}
.hero-title{position:absolute;left:68px;top:280px;font-size:45px;line-height:58px;color:var(--navy);font-weight:400}
.hero-text{position:absolute;left:68px;top:420px;width:520px;font-size:15px;line-height:28px;color:#222}
/* about */
.about-media{position:absolute;left:110px;top:952px;width:412px;height:424px;background:linear-gradient(135deg,#3a4a5c,#8b8f92 55,#c9b8a4)}
.sec-title{font-size:46px;font-weight:400;color:#222}
.kicker{font-size:17px;font-weight:500;color:var(--navy);display:flex;align-items:center;gap:10px}
.kicker .line{width:60px;height:2px;background:var(--navy);position:relative}
.kicker .line::before{content:"";position:absolute;left:0;top:-4px;width:10px;height:10px;background:var(--navy)}
.about-copy{position:absolute;left:590px;top:1052px;width:520px;font-size:13px;line-height:25px;color:#333}
.about-copy p{margin-bottom:24px}
/* band */
.band{position:absolute;top:1478px;left:0;width:1200px;height:358px;background:var(--navy);text-align:center;color:var(--white)}
.band p{position:absolute;left:100px;width:1000px;top:70px;font-size:23px;line-height:36px;font-weight:300}
.band h2{position:absolute;left:100px;width:1000px;top:185px;font-size:30px;line-height:38px;font-weight:600;text-transform:uppercase}
/* services */
.center{text-align:center;position:absolute;left:0;width:1200px}
.svc-node{position:absolute;width:100px;height:100px;border-radius:50%;border:5px solid #fff;box-shadow:0 0 0 2px #e7e7e7,0 4px 12px rgba(0,0,0,.12);display:flex;align-items:center;justify-content:center}
.svc-node.navy{background:var(--navy)}
.svc-node.teal{background:var(--teal)}
.svc-label{position:absolute;font-size:15px;line-height:19px;color:#222}
/* tech */
.tech-copy{position:absolute;left:70px;width:470px;font-size:13px;line-height:25px;color:#333}
.tech-link{color:var(--teal);font-size:15px}
.tile{position:absolute;border:12px solid var(--navy);background:#fff;display:flex;align-items:center;justify-content:center;text-align:center;font-family:"Oswald",sans-serif;color:var(--navy);font-weight:600;font-size:30px;line-height:42px}
.tile.teal{border-color:var(--teal)}
/* blog */
.blog{position:absolute;top:3610px;left:0;width:1200px;height:820px;background:var(--light)}
.card{position:absolute;top:180px;width:330px;height:495px;background:#fff;padding:10px}
.card .media{height:240px}
.card .date{color:var(--teal);font-size:12px;margin:14px 0 6px 6px}
.card h3{font-size:15px;line-height:24px;font-weight:600;color:var(--navy);margin:0 6px}
.card .tags{font-size:12px;font-style:italic;color:#444;margin:8px 6px}
.card .excerpt{font-size:13px;line-height:24px;color:#333;margin:0 6px}
.arrow-btn{position:absolute;width:34px;height:34px;border-radius:50%;border:1.5px solid var(--navy);background:#fff;display:flex;align-items:center;justify-content:center;color:var(--navy)}
/* contact */
.field{position:absolute;height:58px;border:1px solid #eee;box-shadow:0 2px 6px rgba(0,0,0,.06);background:#fff;font-size:15px;color:#666;padding:18px 28px}
/* footer */
.footer{position:absolute;top:5020px;left:0;width:1200px;height:320px;background:var(--navy);color:#fff}
.footer h4{position:absolute;top:82px;font-size:15px;font-weight:500;display:flex;align-items:center;gap:18px}
.footer h4::before{content:"";width:9px;height:9px;background:#fff}
.footer .vr{position:absolute;top:40px;width:1px;height:240px;background:rgba(255,255,255,.35)}
.footer ul{list-style:none;position:absolute;top:128px;font-size:14px;line-height:26px}
.footer ul li::before{content:"▣ ";font-size:11px}
.c-row{position:absolute;left:625px;display:flex;gap:18px;font-size:12px;line-height:16px}
.c-row .ic{width:28px;height:28px;border:1px solid #fff;display:flex;align-items:center;justify-content:center}
.copyright{position:absolute;top:5340px;left:0;width:1200px;height:27px;background:var(--teal);color:#fff;font-size:11px;text-align:center;line-height:27px}
</style>
</head>
<body>

<header class="site-header">
  <div class="brand"><div class="mark"></div><span>qorvanta</span></div>
  <nav class="nav"><span class="active">Home</span><span>Services</span><span>About</span><span>Blog</span></nav>
  <div class="nav-contact">Contact</div>
</header>

<section class="hero">
  <div class="hero-media" role="img" aria-label="Hands typing on a laptop with glowing blue code and web technology icons"></div>
  <h1 class="hero-title">RELIABLE SMART<br>SOFTWARE ENGINEERING</h1>
  <p class="hero-text">We have been on a mission to make complex custom enterprise integration accessible to any organisation, regardless of industry, size, or location.</p>
  <div class="btn" style="left:68px;top:544px">Contact us <span class="sq"><i></i><i></i><i></i><i></i></span></div>
</section>

<section class="about">
  <div class="about-media" role="img" aria-label="Software engineer reviewing code on a screen, framed by square panels"></div>
  <h2 class="sec-title abs" style="left:588px;top:930px">About Us</h2>
  <div class="kicker abs" style="left:590px;top:994px">WHO WE ARE <span class="line"></span></div>
  <div class="about-copy">
    <p>Welcome to Qorvanta!</p>
    <p>Since our inception in 2013, we have been on a mission to make complex custom enterprise integration accessible to any organization, regardless of industry, size, or location.</p>
    <p>Our journey began with a focus on Integration Architecture, quickly moving into delivering bespoke systems integration using Stratavon technologies like LinkForge, CoreFrame, DataVault Server, and WSLink.</p>
  </div>
  <div class="btn" style="left:590px;top:1311px">Know more <span class="sq"><i></i><i></i><i></i><i></i></span></div>
</section>

<section class="band">
  <p>At Qorvanta, we craft bespoke software solutions that are not available on the market. By building organizations market-leading products, process automation, legacy system enablement, or advanced intelligent systems</p>
  <h2>We empower our customers to achieve a competitive edge in their industry.</h2>
  <div class="btn" style="left:522px;top:283px;background:var(--teal)">Contact us <span class="sq"><i></i><i></i><i></i><i></i></span></div>
</section>

<section class="services">
  <h2 class="sec-title center" style="top:1890px">Our Services</h2>
  <div class="kicker abs" style="left:450px;top:1958px;width:300px;justify-content:center">
    <span class="line" style="transform:scaleX(-1)"></span>WHAT WE DO<span class="line"></span>
  </div>
  <svg class="abs" style="left:300px;top:2150px" width="600" height="600" viewBox="0 0 600 600" aria-hidden="true">
    <circle cx="300" cy="300" r="290" fill="none" stroke="#ececec" stroke-width="2"/>
    <circle cx="300" cy="300" r="220" fill="#fff" stroke="#eaeaea" stroke-width="14"/>
    <g fill="var(--navy)">
      <circle cx="358" cy="70" r="4"/><circle cx="502" cy="170" r="4"/><circle cx="532" cy="360" r="4"/>
      <circle cx="434" cy="517" r="4"/><circle cx="248" cy="528" r="4"/><circle cx="110" cy="440" r="4"/>
      <circle cx="66" cy="268" r="4"/><circle cx="142" cy="122" r="4"/>
    </g>
  </svg>
  <div class="abs" role="img" aria-label="Abstract glowing circuit display with square frame motif" style="left:400px;top:2250px;width:400px;height:400px;border-radius:50%;background:radial-gradient(circle at 50% 45%,#3b6a7a 0%,#1f3440 55%,#7a6a3a 100%)"></div>

  <div class="svc-node navy" style="left:627px;top:2089px"><svg width="50" height="40" viewBox="0 0 50 40"><g fill="none" stroke="#fff" stroke-width="2"><circle cx="10" cy="8" r="3"/><circle cx="25" cy="8" r="3"/><circle cx="40" cy="8" r="3"/><circle cx="10" cy="20" r="4"/><circle cx="25" cy="20" r="4"/><circle cx="40" cy="20" r="4"/><circle cx="10" cy="32" r="3"/><circle cx="25" cy="32" r="3"/><circle cx="40" cy="32" r="3"/></g></svg></div>
  <div class="svc-label" style="left:750px;top:2110px">Enterprise Systems<br>&nbsp;Integration</div>

  <div class="svc-node teal" style="left:333px;top:2139px"><span style="color:#fff;font-size:13px;font-weight:600">glidely</span></div>
  <div class="svc-label" style="left:250px;top:2176px">Glidely</div>

  <div class="svc-node teal" style="left:829px;top:2243px"><svg width="46" height="46" viewBox="0 0 46 46"><g fill="none" stroke="#fff" stroke-width="2"><circle cx="23" cy="23" r="6"/><circle cx="23" cy="5" r="3"/><circle cx="23" cy="41" r="3"/><circle cx="5" cy="23" r="3"/><circle cx="41" cy="23" r="3"/><circle cx="10" cy="10" r="3"/><circle cx="36" cy="36" r="3"/><circle cx="36" cy="10" r="3"/><circle cx="10" cy="36" r="3"/><path d="M23 8v9M23 29v9M8 23h9M29 23h9"/></g></svg></div>
  <div class="svc-label" style="left:943px;top:2284px">Microservices</div>

  <div class="svc-node navy" style="left:229px;top:2348px"><svg width="50" height="46" viewBox="0 0 50 46"><g fill="none" stroke="#fff" stroke-width="2"><path d="M12 24a8 8 0 0 1 2-15 11 11 0 0 1 21 2 7 7 0 0 1 1 13z"/><path d="M25 24v10M14 24v10M36 24v10"/><circle cx="14" cy="38" r="3"/><circle cx="25" cy="38" r="3"/><circle cx="36" cy="38" r="3"/></g></svg></div>
  <div class="svc-label" style="left:60px;top:2385px;text-align:right;width:152px">Real-time Data<br>Stream Processing</div>

  <div class="svc-node navy" style="left:869px;top:2477px"><svg width="50" height="42" viewBox="0 0 50 42"><g fill="none" stroke="#fff" stroke-width="2"><path d="M12 28a9 9 0 0 1 2-17 12 12 0 0 1 23 2 8 8 0 0 1 1 15z"/><circle cx="25" cy="20" r="5"/><path d="M25 28v8M18 36h14"/></g></svg></div>
  <div class="svc-label" style="left:990px;top:2507px">Platform<br>Engineering</div>

  <div class="svc-node teal" style="left:277px;top:2581px"><svg width="44" height="44" viewBox="0 0 44 44"><g fill="none" stroke="#fff" stroke-width="2.2"><rect x="9" y="12" width="26" height="22" rx="8"/><circle cx="17" cy="22" r="2.5"/><circle cx="27" cy="22" r="2.5"/><path d="M22 4v8M4 20v8M40 20v8"/></g></svg></div>
  <div class="svc-label" style="left:180px;top:2638px">A.I. Agents</div>

  <div class="svc-node teal" style="left:737px;top:2679px"><svg width="46" height="46" viewBox="0 0 46 46"><g fill="none" stroke="#fff" stroke-width="2"><path d="M23 6v34M14 10v26M32 10v26M7 18h32M7 28h32"/><circle cx="23" cy="23" r="5"/></g></svg></div>
  <div class="svc-label" style="left:857px;top:2722px">Conversational A.I.</div>

  <div class="svc-node navy" style="left:496px;top:2718px"><svg width="50" height="46" viewBox="0 0 50 46"><g fill="none" stroke="#fff" stroke-width="2"><path d="M12 22a8 8 0 0 1 2-15 11 11 0 0 1 21 2 7 7 0 0 1 1 13z"/><path d="M25 22v8M14 30h22M14 30v6M36 30v6M25 30v6"/><circle cx="14" cy="39" r="3"/><circle cx="25" cy="39" r="3"/><circle cx="36" cy="39" r="3"/></g></svg></div>
  <div class="svc-label" style="left:290px;top:2764px;text-align:right;width:183px">Integration Platform<br>as a service (iPaaS)</div>
</section>

<section class="tech">
  <h2 class="sec-title abs" style="left:68px;top:2948px;line-height:50px">Our Technology<br>Expertise <span style="display:inline-block;width:70px;height:2px;background:var(--navy);vertical-align:middle;position:relative"></span></h2>
  <h3 class="abs" style="left:70px;top:3105px;font-size:29px;font-weight:500">STRATAVON</h3>
  <div class="tech-copy" style="top:3170px">We excel in leveraging the Stratavon ecosystem to provide powerful and efficient solutions, including:</div>
  <div class="tech-copy" style="top:3245px"><div class="tech-link">Cirrusly Public Cloud Services</div>Utilizing the full spectrum of Cirrusly services for robust cloud solutions</div>
  <div class="tech-copy" style="top:3320px"><div class="tech-link">Cirrusly DevFlow</div>Streamlining application lifecycle management</div>
  <div class="btn" style="left:72px;top:3414px">Know more <span class="sq"><i></i><i></i><i></i><i></i></span></div>

  <div class="tile" style="left:580px;top:2958px;width:256px;height:174px">PROFICIENCY<br>IN OTHER<br>TECHNOLOGIES</div>
  <div class="tile" style="left:879px;top:2952px;width:256px;height:350px;padding:0"><div role="img" aria-label="Developer working on a laptop with floating technology badges" style="width:100%;height:100%;background:linear-gradient(160deg,#8fb0c4,#c9b39a 60%,#6e8ea6)"></div></div>
  <div class="tile teal" style="left:580px;top:3172px;width:256px;height:350px;padding:0"><div role="img" aria-label="Hands typing on a laptop keyboard with blue glowing light" style="width:100%;height:100%;background:linear-gradient(160deg,#e3ecf4,#8fb7dd 55%,#3f6fa8)"></div></div>
  <div class="tile teal" style="left:880px;top:3343px;width:256px;height:170px">STRATAVON</div>
</section>

<section class="blog">
  <h2 class="sec-title center" style="top:80px">Our Blog</h2>
  <div class="kicker abs" style="left:480px;top:140px;width:240px;justify-content:center;font-size:16px">
    <span class="line" style="width:30px;transform:scaleX(-1)"></span>NEWS &amp; UPDATES<span class="line" style="width:30px"></span>
  </div>
  <div class="arrow-btn" style="left:17px;top:455px">‹</div>
  <div class="arrow-btn" style="left:1153px;top:455px">›</div>

  <article class="card" style="left:75px">
    <div class="media" role="img" aria-label="Rows of server racks in a data centre" style="background:linear-gradient(90deg,#1c2a22,#4e7d4a 50%,#1c2a22)"></div>
    <div class="date">▦ June 24, 2024</div>
    <h3>Why most upgrade paths for LinkForge lead to using Cirrusly Flow apps</h3>
    <div class="tags">Integration, LinkForge</div>
    <p class="excerpt">Introduction In today's fast-evolving technological landscape, businesses</p>
    <div class="btn sm" style="left:16px;top:452px">Know more <span class="sq"><i></i><i></i><i></i><i></i></span></div>
  </article>

  <article class="card" style="left:435px">
    <div class="media" role="img" aria-label="Team meeting around a table with integration diagram overlay" style="background:linear-gradient(135deg,#d9dde2,#8b929a 60%,#3d444c)"></div>
    <div class="date">▦ June 21, 2024</div>
    <h3>Meet Qorvanta: The LinkForge Experts</h3>
    <div class="tags">Integration, LinkForge, Stratavon</div>
    <p class="excerpt">At Qorvanta, we pride ourselves on having a team of exceptional talent,</p>
    <div class="btn sm" style="left:16px;top:428px">Know more <span class="sq"><i></i><i></i><i></i><i></i></span></div>
  </article>

  <article class="card" style="left:795px">
    <div class="media" role="img" aria-label="Illustration of server hardware next to stacked paperwork" style="background:linear-gradient(90deg,#e6e6e6,#3a3f55 40%,#c23a3a 60%,#ead9b0)"></div>
    <div class="date">▦ June 24, 2024</div>
    <h3>Top Reasons LinkForge Server Runtime Can Fail in Production</h3>
    <div class="tags">Integration, LinkForge</div>
    <p class="excerpt">As a LinkForge expert with extensive experience in deploying and maintaining</p>
    <div class="btn sm" style="left:16px;top:452px">Know more <span class="sq"><i></i><i></i><i></i><i></i></span></div>
  </article>
</section>

<section class="contact">
  <div class="abs" style="left:0;top:4430px;width:243px;height:590px;background:var(--teal)"></div>
  <div class="abs" role="img" aria-label="Person holding a mug in front of a screen with data dashboards" style="left:72px;top:4545px;width:408px;height:380px;background:linear-gradient(120deg,#e8e4de,#9aa3ad 50%,#2c3644)"></div>
  <h2 class="sec-title abs" style="left:566px;top:4475px">Contact Us</h2>
  <div class="abs" style="left:573px;top:4540px;font-size:17px;font-weight:500;color:var(--navy)">QORVANTA</div>
  <div class="abs" style="left:577px;top:4600px;font-size:12px;color:#333">Fill out our form and we'll be in touch.</div>
  <div class="field" style="left:573px;top:4640px;width:270px">First Name</div>
  <div class="field" style="left:862px;top:4640px;width:272px">Last Name</div>
  <div class="field" style="left:573px;top:4718px;width:270px">Mobile Number</div>
  <div class="field" style="left:862px;top:4718px;width:272px">Email Address</div>
  <div class="field" style="left:573px;top:4796px;width:561px;height:95px">Message</div>
  <div class="btn" style="left:573px;top:4925px">Submit <span class="sq"><i></i><i></i><i></i><i></i></span></div>
</section>

<footer class="footer">
  <div class="abs" style="left:70px;top:80px;display:flex;align-items:center;gap:12px">
    <div style="width:30px;height:30px;border:2px solid #fff"></div><span style="font-size:22px">qorvanta</span>
  </div>
  <p class="abs" style="left:68px;top:150px;width:220px;font-size:12px;line-height:22px">We have been on a mission to make complex custom enterprise integration accessible to any organisation.</p>
  <div class="abs" style="left:78px;top:248px;display:flex;gap:6px">
    <span style="width:28px;height:28px;border-radius:50%;background:var(--teal)"></span>
    <span style="width:28px;height:28px;border-radius:50%;border:1.5px solid #fff"></span>
    <span style="width:28px;height:28px;border-radius:50%;border:1.5px solid #fff"></span>
  </div>
  <div class="vr" style="left:340px"></div>
  <div class="vr" style="left:540px"></div>
  <div class="vr" style="left:890px"></div>
  <h4 style="left:335px">QUICK LINKS</h4>
  <ul style="left:375px"><li>Home</li><li>Services</li><li>Contact</li><li>About</li><li>Blog</li></ul>
  <h4 style="left:535px">CONTACT US</h4>
  <div class="c-row" style="top:130px"><span class="ic">☏</span><span>CALL US<br>1800 555 019</span></div>
  <div class="c-row" style="top:182px"><span class="ic">✉</span><span>EMAIL US<br>info@qorvanta.com</span></div>
  <div class="c-row" style="top:234px"><span class="ic">⌖</span><span>Suite 210, 48 Harbour Lane<br>Melbourne, VIC , 3000</span></div>
  <h4 style="left:887px">NEWSLETTER SIGN UP</h4>
  <p class="abs" style="left:928px;top:142px;width:220px;font-size:12px;line-height:17px">Subscribe our newsletter to get the latest news.</p>
  <div class="abs" style="left:920px;top:188px;width:204px;height:34px;border:1px solid #fff;border-radius:17px;font-size:11px;padding:9px 16px">Enter Email Address</div>
  <div class="abs" style="left:1094px;top:194px;width:22px;height:22px;border:1px solid #fff;border-radius:50%;font-size:12px;text-align:center;line-height:20px">→</div>
</footer>
<div class="copyright">Copyright © 2025 All Rights Reserved By Company name|privacy policy</div>

</body>
</html>
```